Business card - mobile service

O KiraTel is a mobile family safety service based on tablets and smartphones.
The business card must have:
BASIC INFO
Company Logo
Name
Position / Job Title: Co-founder
Mobile Phone Number: +55 (11) 5080 6172
Land Line: +55 (11) 9087 614352
Email Address: name@kiratel-example.com
Web Site URL: www.kiratel-example.com
PROMOTIONAL INFO
Try KiraTel free Today!
Your personal promo code: xxxx-2222-uuuu-7777-1234
Promo code text explanation with the instructions about the trial offer
Updates
Dears,
One more must have: the KiraTel slogan:
Industry/Entity Type
Safety
Look and feel
Each slider illustrates characteristics of the customer's brand and the style your logo design should communicate.

```html
<!DOCTYPE html>
<html lang="en">
<head>
<meta charset="utf-8">
<title>KiraTel business card</title>
<link rel="stylesheet" href="https://fonts.googleapis.com/css2?family=Arimo:wght@400;700&display=swap">
<style>
  :root {
    --stage: #3a3a3c;
    --card: #ffffff;
    --brand-blue: #1ea3e0;
    --brand-yellow: #fdb813;
    --band-dark: #1877b8;
    --band-light: #45b6ea;
    --ink-grey: #8a8a8a;
    --ink-dark: #333333;
  }
  * { box-sizing: border-box; margin: 0; padding: 0; }
  html, body { width: 1200px; height: 900px; overflow: hidden; }
  body {
    background: var(--stage);
    font-family: "Arimo", Arial, sans-serif;
    position: relative;
  }
  .card {
    position: absolute;
    background: var(--card);
    border-radius: 16px;
    overflow: hidden;
    box-shadow: 0 6px 18px rgba(0,0,0,.45);
  }
  .card--front-white { left: 27px; top: 82px; width: 558px; height: 308px; }
  .card--front-blue {
    left: 607px; top: 82px; width: 568px; height: 308px;
    background: linear-gradient(to bottom, var(--brand-blue) 0%, #bfe6f8 28%, #ffffff 45%, #ffffff 60%, #bfe6f8 75%, var(--brand-blue) 100%);
  }
  .card--back { left: 222px; top: 474px; width: 693px; height: 384px; }

  .brand { position: absolute; left: 0; right: 0; text-align: center; }
  .brand__name {
    display: inline-flex; align-items: center; gap: 14px;
    font-weight: 700; color: var(--brand-blue); letter-spacing: -2px; line-height: 1;
  }
  .brand__dot { border-radius: 50%; background: var(--brand-yellow); display: inline-block; }
  .brand__slogan { font-weight: 700; color: var(--brand-blue); line-height: 1; white-space: nowrap; }

  .card--front-white .brand, .card--front-blue .brand { top: 72px; }
  .card--front-white .brand__name, .card--front-blue .brand__name { font-size: 118px; }
  .card--front-white .brand__dot, .card--front-blue .brand__dot { width: 46px; height: 46px; }
  .card--front-white .brand__slogan, .card--front-blue .brand__slogan { font-size: 34px; margin-top: 14px; }

  .card--back .brand { top: 34px; left: 0; width: 580px; }
  .card--back .brand__name { font-size: 60px; gap: 8px; letter-spacing: -1px; }
  .card--back .brand__dot { width: 24px; height: 24px; }
  .card--back .brand__slogan { font-size: 20px; margin-top: 8px; }

  .person { position: absolute; top: 186px; left: 0; width: 580px; text-align: center; }
  .person__name { font-size: 24px; color: var(--brand-blue); }
  .person__role { font-size: 16px; color: var(--ink-grey); margin-top: 4px; }

  .contacts { position: absolute; left: 40px; top: 316px; width: 530px; height: 50px; font-size: 15px; color: var(--ink-dark); }
  .contact { position: absolute; display: flex; align-items: center; gap: 8px; white-space: nowrap; line-height: 20px; }
  .contact svg { fill: var(--brand-blue); flex: none; }
  .contact--landline { left: 0; top: 0; }
  .contact--mobile { left: 292px; top: 0; }
  .contact--email { left: 50px; top: 26px; }
  .contact--web { left: 288px; top: 26px; }

  .promo-band {
    position: absolute; left: 580px; top: 0; width: 75px; height: 384px;
    background: linear-gradient(to right, var(--band-dark), var(--band-light) 55%, var(--band-dark));
  }
  .promo-band__text {
    position: absolute; left: 50%; top: 50%;
    width: 370px; transform: translate(-50%, -50%) rotate(-90deg);
    color: #ffffff; text-align: left; line-height: 1.2;
  }
  .promo-band__title { font-size: 15px; font-weight: 700; }
  .promo-band__code { font-size: 11.5px; margin-top: 6px; }
  .promo-band__note { font-size: 8px; margin-top: 3px; opacity: .9; }
</style>
</head>
<body>
  <section class="card card--front-white">
    <div class="brand">
      <div class="brand__name">KiraTel<span class="brand__dot"></span></div>
      <div class="brand__slogan">Your Family Safety Service</div>
    </div>
  </section>

  <section class="card card--front-blue">
    <div class="brand">
      <div class="brand__name">KiraTel<span class="brand__dot"></span></div>
      <div class="brand__slogan">Your Family Safety Service</div>
    </div>
  </section>

  <section class="card card--back">
    <div class="brand">
      <div class="brand__name">KiraTel<span class="brand__dot"></span></div>
      <div class="brand__slogan">Your Family Safety Service</div>
    </div>

    <div class="person">
      <div class="person__name">Your Name Here</div>
      <div class="person__role">Principal</div>
    </div>

    <div class="contacts">
      <div class="contact contact--landline">
        <svg width="22" height="16" viewBox="0 0 22 16"><path d="M1 5c3-4 17-4 20 0l-1 3-4-1V5H6v2L2 8z"/><rect x="5" y="9" width="12" height="6" rx="1.5"/></svg>
        <span>+55 (11) 9087 614352</span>
      </div>
      <div class="contact contact--mobile">
        <svg width="12" height="20" viewBox="0 0 12 20"><rect x="1" y="1" width="10" height="18" rx="2" fill="none" stroke="var(--brand-blue)" stroke-width="2"/><rect x="3" y="4" width="6" height="8"/></svg>
        <span>+55 (11) 5080 6172</span>
      </div>
      <div class="contact contact--email">
        <svg width="18" height="13" viewBox="0 0 18 13"><rect width="18" height="13" rx="2"/></svg>
        <span>name@kiratel-example.com</span>
      </div>
      <div class="contact contact--web">
        <svg width="20" height="20" viewBox="0 0 20 20"><circle cx="10" cy="10" r="8.5" fill="none" stroke="var(--brand-blue)" stroke-width="2"/><path d="M5 6h2l1.5 6L10 7l1.5 5L13 6h2l-2.7 9h-1.6L10 11l-0.7 4H7.7z"/></svg>
        <span>www.kiratel-example.com</span>
      </div>
    </div>

    <aside class="promo-band">
      <div class="promo-band__text">
        <div class="promo-band__title">Try KiraTel free Today!</div>
        <div class="promo-band__code">Your personal promo code: xxxx-2222-uuuu-7777-1234</div>
        <div class="promo-band__note">Promo code text explanation with the instructions about the trial offer</div>
      </div>
    </aside>
  </section>
</body>
</html>
```